Dr Fobu smart screen Flyer design

Hi,

Please see attached file as I have done up a very very basic flyer just with the information that will need to be presented.

Please don't go with this as a format I would like, as I have no design skills at all.

I'm looking for something that is basic but professional looking capturing this information.
I would prefer if the symbols were changed so they were all consistent and the colour scheme worked together with the logo.

If you can use the picture of the screen provided as I will replace this once my product has its photoshoot.

Thanks!

```html
<!DOCTYPE html>
<html lang="en">
<head>
<meta charset="utf-8">
<title>Dr Fobu Smart Screen Flyer</title>
<link rel="stylesheet" href="https://fonts.googleapis.com/css2?family=Barlow:wght@400;500;600&display=swap">
<style>
:root{
  --blue-deep:#0a6fb8;
  --blue-mid:#1591d8;
  --blue-bright:#1ea9e6;
  --panel:#d8eef4;
  --sky-top:#a9d8f2;
  --sky-bottom:#dff1f9;
  --magenta:#c0509c;
  --cyan:#4ec8ee;
  --yellow:#ffd800;
  --ink:#1d1d1d;
  --heading:#1a6db4;
  --white:#ffffff;
}
*{margin:0;padding:0;box-sizing:border-box}
html,body{width:1200px;height:1000px;overflow:hidden;background:var(--white)}
body{position:relative;font-family:"Barlow",Arial,sans-serif;color:var(--ink)}
.flyer{position:absolute;left:291px;top:62px;width:620px;height:878px;background:var(--white);box-shadow:0 2px 10px rgba(0,0,0,.18);overflow:hidden}
.header-art{position:absolute;left:0;top:0}
.logo-card{position:absolute;left:0;top:181px;width:273px;height:149px;background:var(--white);box-shadow:8px 0 0 var(--blue-deep);display:flex;flex-direction:column;align-items:center;justify-content:center}
.logo-name{display:flex;align-items:center;gap:8px;font-size:42px;font-weight:500;color:var(--ink);letter-spacing:2px;line-height:1}
.logo-dot{width:10px;height:10px;background:var(--magenta)}
.logo-tag{margin-top:8px;font-size:10px;font-weight:600;letter-spacing:5px;color:var(--ink)}
.headline{position:absolute;left:59px;top:430px;font-size:28.5px;font-weight:600;line-height:34.5px;color:var(--heading)}
.headline em{font-style:normal;color:var(--magenta)}
.intro{position:absolute;left:59px;top:587px;width:223px;font-size:14.5px;font-weight:500;line-height:18.5px;text-align:justify;letter-spacing:0}
.intro p{margin-bottom:19px}
.features{position:absolute;left:325px;top:450px;width:250px}
.feature{position:absolute;left:0;width:250px}
.feature h3{font-size:14.5px;font-weight:600;color:var(--heading);line-height:17px}
.feature p{font-size:9px;line-height:11px;margin-top:4px;width:162px;font-weight:500}
.feature svg{position:absolute;left:177px;top:0}
.footer{position:absolute;left:0;top:788px;width:620px;height:60px;background:linear-gradient(90deg,var(--blue-bright),var(--blue-mid) 60%,var(--blue-deep));color:var(--white);font-size:12px}
.footer span{position:absolute;top:20px}
.footer .phone{left:60px}
.footer .phone small{display:block;font-size:5px;line-height:6px}
.footer .email{left:237px}
.footer .web{left:444px}
.block{position:absolute}
</style>
</head>
<body>
<div class="flyer">
  <svg class="header-art" width="620" height="450" viewBox="0 0 620 450">
    <defs>
      <linearGradient id="sky" x1="0" y1="0" x2="0" y2="1"><stop offset="0" stop-color="var(--sky-top)"/><stop offset="1" stop-color="var(--sky-bottom)"/></linearGradient>
      <linearGradient id="frame" x1="0" y1="0" x2="0" y2="1"><stop offset="0" stop-color="var(--blue-deep)"/><stop offset=".75" stop-color="var(--blue-mid)"/><stop offset="1" stop-color="var(--blue-bright)"/></linearGradient>
      <linearGradient id="screen" x1="0" y1="0" x2="0" y2="1"><stop offset="0" stop-color="#8fb6c8"/><stop offset=".45" stop-color="#a6b98a"/><stop offset="1" stop-color="#6fa035"/></linearGradient>
    </defs>
    <polygon points="0,0 620,0 620,443 0,398" fill="url(#sky)"/>
    <polygon points="0,88 620,0 620,443 0,398" fill="url(#frame)"/>
    <polygon points="36,138 586,42 586,404 36,393" fill="var(--panel)"/>
    <g role="img" aria-label="Photo of an outdoor LED screen cabinet showing children running across a meadow">
      <polygon points="301,120 521,73 521,403 301,350" fill="url(#screen)"/>
      <polygon points="521,73 569,86 569,378 521,403" fill="#1f2426"/>
    </g>
    <rect x="36" y="31" width="34" height="26" fill="var(--cyan)"/>
    <rect x="106" y="30" width="72" height="54" fill="var(--magenta)"/>
    <rect x="87" y="69" width="34" height="26" fill="var(--magenta)"/>
    <rect x="30" y="102" width="22" height="14" fill="var(--yellow)"/>
    <rect x="42" y="110" width="32" height="24" fill="var(--yellow)"/>
  </svg>

  <div class="logo-card">
    <div class="logo-name"><span class="logo-dot"></span>Dr Fobu</div>
    <div class="logo-tag">SMART SCREEN</div>
  </div>

  <h1 class="headline">Bring attention<br>to your business<br>with your own<br><em>HD LED</em> display</h1>

  <div class="intro">
    <p>Our displays can be mounted outdoors on walls, roofs, fixed signs, trailer mounted ect.</p>
    <p>We also do indoor LED screens for shop fronts and display stands.</p>
    <p>All screens are cumtom built to your requirements including size, shape and even curved displays.</p>
  </div>

  <div class="features">
    <div class="feature" style="top:0">
      <h3>4G Capable</h3>
      <p>Change screen content with a click of the mouse anywhere in the world</p>
      <svg width="62" height="46" viewBox="0 0 62 46"><path d="M44 14V4H2v40h56V30" fill="none" stroke="var(--heading)" stroke-width="3"/><text x="8" y="36" font-family="Barlow,sans-serif" font-weight="600" font-size="20" fill="var(--heading)">4G</text><path d="M44 10a12 12 0 0 1 12 12M44 4a18 18 0 0 1 18 18" fill="none" stroke="var(--yellow)" stroke-width="2.5"/><path d="M44 16a6 6 0 0 1 6 6" fill="none" stroke="var(--magenta)" stroke-width="2.5"/></svg>
    </div>
    <div class="feature" style="top:58px">
      <h3>Wifi Capable</h3>
      <p>Change screen content with a PC, tablet or mobile phone with an easy to use app</p>
      <svg width="62" height="46" viewBox="0 0 62 46"><path d="M40 6H2v38h56V28" fill="none" stroke="var(--heading)" stroke-width="3"/><circle cx="28" cy="32" r="4" fill="var(--magenta)"/><path d="M28 22a10 10 0 0 1 10 10" fill="none" stroke="var(--magenta)" stroke-width="3"/><path d="M28 14a18 18 0 0 1 18 18" fill="none" stroke="var(--cyan)" stroke-width="3"/><path d="M28 6a26 26 0 0 1 26 26" fill="none" stroke="var(--yellow)" stroke-width="3"/></svg>
    </div>
    <div class="feature" style="top:117px">
      <h3>Inteligent brightness<br>control</h3>
      <p>Screen will automatically adjust to suit ambiant light improving screen veiwing quality and saving in power consumption</p>
      <svg width="62" height="46" viewBox="0 0 62 46" style="top:10px"><path d="M2 6h56v38H2z" fill="none" stroke="var(--heading)" stroke-width="3"/><circle cx="30" cy="25" r="7" fill="var(--yellow)"/><path d="M30 25v-7a7 7 0 0 0 0 14z" fill="var(--heading)"/><path d="M30 11v4M30 35v4M16 25h4M40 25h4M20 15l3 3M37 32l3 3M40 15l-3 3M20 35l3-3" stroke="var(--yellow)" stroke-width="2"/><path d="M6 38h6M48 38h6M51 35v6" stroke="var(--heading)" stroke-width="2"/></svg>
    </div>
    <div class="feature" style="top:203px">
      <h3>Online Monitoring</h3>
      <p>Monitor cabinet temperature and humidity plus more in real time online.</p>
      <p>Recieve alerts via email.</p>
      <svg width="66" height="50" viewBox="0 0 66 50" style="top:6px"><path d="M44 8H2v40h56V26" fill="none" stroke="var(--heading)" stroke-width="3"/><rect x="46" y="2" width="18" height="14" fill="none" stroke="var(--magenta)" stroke-width="1.5"/><path d="M46 2l9 7 9-7" fill="none" stroke="var(--magenta)" stroke-width="1.5"/><rect x="12" y="16" width="5" height="18" rx="2.5" fill="none" stroke="var(--heading)" stroke-width="2"/><circle cx="14.5" cy="37" r="4" fill="var(--magenta)"/><path d="M26 40l10-22" stroke="var(--heading)" stroke-width="2"/><path d="M42 26c3 4 5 7 5 9a5 5 0 0 1-10 0c0-2 2-5 5-9z" fill="var(--cyan)"/></svg>
    </div>
    <div class="feature" style="top:272px">
      <h3>High quality products</h3>
      <p>Setting high standard for colour, brightness and sharpness these LED modules will create attention.</p>
      <svg width="66" height="50" viewBox="0 0 66 50" style="top:-6px"><path d="M44 6H2v42h56V24" fill="none" stroke="var(--heading)" stroke-width="3"/><text x="6" y="24" font-family="Barlow,sans-serif" font-weight="600" font-size="11" fill="var(--heading)">HIGH</text><text x="6" y="38" font-family="Barlow,sans-serif" font-weight="600" font-size="11" fill="var(--heading)">QUALITY</text><path d="M36 14l8 8 18-20" fill="none" stroke="var(--heading)" stroke-width="5"/></svg>
    </div>
  </div>

  <div class="footer">
    <span class="phone">1300 DRFOBU<small>for a free quote</small></span>
    <span class="email">info@drfobu.com.au</span>
    <span class="web">www.drfobu.com.au</span>
  </div>

  <div class="block" style="left:534px;top:778px;width:28px;height:20px;background:var(--cyan)"></div>
  <div class="block" style="left:589px;top:776px;width:31px;height:50px;background:var(--magenta)"></div>
  <div class="block" style="left:574px;top:808px;width:26px;height:18px;background:var(--magenta)"></div>
  <div class="block" style="left:530px;top:833px;width:14px;height:10px;background:var(--yellow)"></div>
  <div class="block" style="left:537px;top:841px;width:28px;height:16px;background:var(--yellow)"></div>
</div>
</body>
</html>
```